Staff Falcons WIX Design Project - website for HR Professional Community

Redesign of website to incorporate new logo - we are looking for a web design partner - will include adhoc work going forward.

Current website - www.thestafffalcons.co.uk

The 'Onward to Vivid' content is not required on the new site.

Target Market(s)

HR professionals

Industry/Entity Type

Professional Network

Coding

Coded - Design and coding required

Requirements
Must have
• A partners page
Nice to have
• an events page

```html
<!DOCTYPE html>
<html lang="en">
<head>
<meta charset="utf-8">
<title>Staff Falcons – Online Community for HR Professionals</title>
<link href="https://fonts.googleapis.com/css2?family=Roboto:ital,wght@0,400;0,500;0,700;1,500&family=Open+Sans:ital,wght@0,400;0,600;1,600&display=swap" rel="stylesheet">
<style>
:root{
  --orange:#f0861d;
  --ink:#1e1e1e;
  --body:#5d5d5d;
  --grey-bg:#f3f3f3;
  --white:#ffffff;
  --footer:#222222;
  --faint:#e9e9e9;
}
*{margin:0;padding:0;box-sizing:border-box}
html,body{width:1200px;height:4979px;overflow:hidden}
body{position:relative;background:var(--white);font-family:"Open Sans",sans-serif;color:var(--body)}
.abs{position:absolute}
.heading{font-family:"Roboto",sans-serif;font-weight:400;color:var(--ink);font-size:40px;line-height:1.1;text-transform:uppercase}
.heading strong{color:var(--orange);font-weight:500}
.center{text-align:center;left:0;width:1200px}
.btn{position:absolute;display:flex;align-items:center;justify-content:center;background:var(--orange);color:var(--white);font-family:"Roboto",sans-serif;font-weight:500;font-size:16px;border-radius:30px;text-transform:uppercase;letter-spacing:.2px;white-space:nowrap}
.side-word{position:absolute;font-family:"Roboto",sans-serif;font-weight:700;font-size:82px;color:var(--faint);white-space:nowrap;transform:rotate(-90deg);transform-origin:left top}

/* hero */
.hero{left:0;top:0;width:1200px;height:750px;background:linear-gradient(180deg,#5f7c95 0%,#8aa0b0 35%,#b9b6aa 60%,#8f8475 85%,#6b6257 100%)}
.brand{left:112px;top:14px;width:200px;text-align:center}
.brand-dot{width:56px;height:56px;border-radius:50%;background:var(--orange);margin:0 auto 10px}
.brand-name{font-family:"Roboto",sans-serif;font-weight:400;font-size:30px;letter-spacing:2px;color:var(--white);white-space:nowrap}
.nav{right:110px;top:64px;display:flex;gap:28px;font-family:"Roboto",sans-serif;font-size:18px;color:var(--white)}
.nav .active{color:var(--orange)}
.top-mail{right:110px;top:16px;font-family:"Roboto",sans-serif;font-size:17px;color:var(--white);display:flex;align-items:center;gap:8px}
.hero-title{top:232px;font-family:"Roboto",sans-serif;font-weight:700;font-size:64px;color:var(--white)}
.hero-sub{top:312px;font-family:"Roboto",sans-serif;font-size:29px;color:var(--white)}

/* welcome */
.welcome-copy{left:665px;top:966px;width:430px;font-size:15px;line-height:28px}
.welcome-copy p+p{margin-top:28px}

/* services */
.service{position:absolute;top:1594px;width:280px;text-align:center}
.service-icon{width:176px;height:176px;border-radius:50%;background:var(--white);box-shadow:0 4px 14px rgba(0,0,0,.08);margin:0 auto}
.service h3{font-family:"Roboto",sans-serif;font-weight:500;font-size:25px;color:var(--ink);margin-top:24px}
.service p{font-size:15px;line-height:26px;margin-top:12px}

/* career */
.career-text{left:112px;color:var(--white)}
.career-title{font-family:"Roboto",sans-serif;font-size:38px;line-height:54px;text-transform:uppercase}
.career-q{font-family:"Open Sans",sans-serif;font-style:italic;font-weight:600;font-size:19px;line-height:24px}

/* testimonial */
.quote{left:483px;top:2840px;width:615px;font-family:"Roboto",sans-serif;font-style:italic;font-weight:500;font-size:24px;line-height:38px;color:var(--ink)}
.arrow-btn{position:absolute;width:40px;height:40px;border-radius:50%;display:flex;align-items:center;justify-content:center}

/* events */
.card{position:absolute;top:3416px;width:464px;height:529px;background:var(--white);box-shadow:0 4px 14px rgba(0,0,0,.1)}
.card-photo{width:464px;height:280px}
.card-body{padding:22px 32px 0}
.card-date{font-size:15px;color:var(--body);display:flex;align-items:center;gap:6px}
.card-title{font-family:"Roboto",sans-serif;font-weight:500;font-size:24px;color:var(--ink);margin-top:8px}
.card-text{font-size:15px;line-height:27px;margin-top:12px}
.card-more{font-family:"Roboto",sans-serif;font-weight:500;font-size:15px;color:var(--orange);margin-top:14px}

/* partners */
.partner{position:absolute;top:4285px;width:188px;height:105px;border:1px solid #dcdcdc;background:var(--white);display:flex;align-items:center;justify-content:center}
.partner.active{border:2px solid var(--orange)}
.partner-shape{background:#c9c9c9}

/* footer */
.footer{left:0;top:4430px;width:1200px;height:549px;background:var(--footer)}
.foot-text{font-size:15px;color:var(--white);line-height:20px}
.foot-title{font-family:"Roboto",sans-serif;font-weight:500;font-size:19px;color:var(--white);line-height:28px}
.foot-links{list-style:none;font-size:15px;color:var(--white);line-height:28px}
.field{position:absolute;width:203px;height:36px;border:1px solid #8a8a8a;color:var(--white);font-size:15px;padding:7px 14px}
.social{position:absolute;width:36px;height:36px;border-radius:50%;border:1px solid var(--orange)}
</style>
</head>
<body>

<!-- hero -->
<div class="abs hero" role="img" aria-label="Photograph of the London city skyline under a blue sky"></div>
<svg class="abs" style="left:0;top:660px" width="1200" height="100" viewBox="0 0 1200 100" aria-hidden="true"><path d="M0 90 Q600 0 1200 90 L1200 100 L0 100 Z" fill="#ffffff"/></svg>
<div class="abs brand"><div class="brand-dot"></div><div class="brand-name">STAFF FALCONS</div></div>
<div class="abs top-mail"><svg width="18" height="13" viewBox="0 0 18 13"><rect width="18" height="13" rx="1" fill="#f0861d"/><path d="M0 1 L9 7 L18 1" stroke="#fff" stroke-width="1.5" fill="none"/></svg>hq@thestafffalcons.co.uk</div>
<nav class="abs nav"><span class="active">Home</span><span>Our Story</span><span>Newsletter</span><span>Events</span><span>Partners</span><span>Contact</span></nav>
<div class="abs center hero-title">The UK's most vibrant</div>
<div class="abs center hero-sub">online community for HR Professionals</div>
<div class="btn" style="left:406px;top:370px;width:386px;height:62px;font-size:18px">Sign up here for our newsletter</div>

<!-- welcome -->
<div class="abs" style="left:112px;top:802px;width:489px;height:527px;background:linear-gradient(135deg,#c9d6e0,#a9b8c4 50%,#8fa1ad)" role="img" aria-label="Photograph of colleagues stacking their fists together, tagged #strongertogether"></div>
<div class="abs heading" style="left:665px;top:836px"><strong>Welcome to</strong></div>
<div class="abs heading" style="left:665px;top:890px">The Staff Falcons!</div>
<div class="abs welcome-copy">
  <p>"Don't do it." They said. "It'll never work". They said. "No one will be interested". They said. "Isn't ProLink better for that sort of thing?" They said. You see back in 2017 HR Circlebook communities weren't a really a thing. It was unchartered territory.</p>
  <p>But I had a gut feeling that we might be onto something so we started small, with just 30 members.</p>
</div>
<div class="btn" style="left:665px;top:1230px;width:152px;height:56px">Read more</div>

<!-- services -->
<svg class="abs" style="left:0;top:1380px" width="1200" height="740" viewBox="0 0 1200 740" aria-hidden="true"><path d="M0 20 Q600 -20 1200 20 L1200 700 Q600 640 0 720 Z" fill="#f3f3f3"/></svg>
<div class="side-word" style="left:1120px;top:1960px">Services</div>
<div class="abs heading center" style="top:1516px"><strong>What</strong> we do</div>

<div class="service" style="left:107px">
  <div class="service-icon" role="img" aria-label="Illustration of a group of community members"></div>
  <h3>Community</h3>
  <p>Our Circlebook Community Group enables you to connect with a fast-growing, highly engaged community of over 17k HR professionals</p>
</div>
<div class="service" style="left:459px">
  <div class="service-icon" role="img" aria-label="Illustration of a member holding a briefcase"></div>
  <h3>Jobs</h3>
  <p>Get your HR job in front of 17k HR Professionals FREE job postings for members of our Circlebook group Open to non-members ONLY £100+vat</p>
</div>
<div class="service" style="left:809px">
  <div class="service-icon" role="img" aria-label="Illustration of a member beside gear wheels"></div>
  <h3>Coaching</h3>
  <p>Our coaching club is currently over subscribed and we are not currently accepting requests for support. Doors are open now for registrations</p>
</div>
<div class="btn" style="left:118px;top:1964px;width:260px;height:56px;font-size:15px">Join our Circlebook group</div>
<div class="btn" style="left:482px;top:1964px;width:260px;height:56px;font-size:15px">View our jobs board</div>
<div class="btn" style="left:820px;top:1964px;width:260px;height:56px;font-size:15px">Join our coaching club</div>

<!-- career -->
<svg class="abs" style="left:0;top:2096px" width="1200" height="656" viewBox="0 0 1200 656" aria-hidden="true">
  <defs><linearGradient id="careerFade" x1="0" x2="1" y1="0" y2="0">
    <stop offset="0" stop-color="#f0861d"/><stop offset=".42" stop-color="#f0861d"/>
    <stop offset=".55" stop-color="#e6a25a"/><stop offset=".8" stop-color="#c89c74"/><stop offset="1" stop-color="#a99583"/>
  </linearGradient></defs>
  <path d="M0 90 Q600 -60 1200 50 L1200 656 L0 656 Z" fill="url(#careerFade)"/>
</svg>
<div class="abs" style="left:640px;top:2130px;width:560px;height:621px" role="img" aria-label="Photograph of a smiling woman working on a laptop"></div>
<div class="side-word" style="left:10px;top:2600px;color:rgba(255,255,255,.18)">Career</div>
<div class="abs career-text career-title" style="top:2195px;font-weight:700">Job Board!</div>
<div class="abs career-text career-title" style="top:2249px">Job Board!</div>
<div class="abs career-text career-q" style="top:2336px;width:460px">Are you looking to share your HR roles with our audience?</div>
<div class="abs career-text career-q" style="top:2408px;width:460px;left:118px">Are you an HR job seeker looking for your next adventure?</div>
<div class="abs career-text" style="top:2472px;width:470px;font-weight:600;font-size:25px;line-height:35px">We are fast becoming THE place to share and seek for HR jobs in the UK</div>
<div class="abs career-text" style="top:2558px;width:420px;font-size:14px;line-height:24px">(and get this!... If you're a member of our Circlebook group you can share your jobs for FREE!)</div>
<div class="btn" style="left:112px;top:2640px;width:153px;height:52px;background:#fff;color:var(--ink);font-size:16px">View jobs</div>

<!-- testimonials -->
<div class="side-word" style="left:1110px;top:3145px">Reviews</div>
<div class="abs heading" style="left:110px;top:2944px"><strong>Client</strong></div>
<div class="abs heading" style="left:110px;top:2998px">Testimonials</div>
<div class="abs quote">“ I came across the Staff Falcons community on Circlebook and truly believe that the timing of this was meant to be because I asked for some advice relating to a role I was applying for and 8 days later I landed the job! I am blown away by the support in this group”</div>
<div class="abs" style="left:488px;top:3062px;font-size:17px">- Sam. HR Professional</div>
<div class="arrow-btn" style="left:496px;top:3122px;background:#cfcfcf"><svg width="12" height="18" viewBox="0 0 12 18"><path d="M9 2 L3 9 L9 16" stroke="#fff" stroke-width="2" fill="none"/></svg></div>
<div class="arrow-btn" style="left:546px;top:3122px;background:var(--orange)"><svg width="12" height="18" viewBox="0 0 12 18"><path d="M3 2 L9 9 L3 16" stroke="#fff" stroke-width="2" fill="none"/></svg></div>

<!-- events -->
<svg class="abs" style="left:0;top:3190px" width="1200" height="1020" viewBox="0 0 1200 1020" aria-hidden="true"><path d="M0 30 Q600 -20 1200 30 L1200 990 Q600 1040 0 990 Z" fill="#f3f3f3"/></svg>
<div class="side-word" style="left:8px;top:3820px">Events</div>
<div class="abs heading center" style="top:3322px"><strong>Latest</strong> events</div>

<div class="card" style="left:112px">
  <div class="card-photo" style="background:linear-gradient(135deg,#8e9aa3,#c7c3ba 55%,#6f7a82)" role="img" aria-label="Photograph of an audience applauding at an event"></div>
  <div class="card-body">
    <div class="card-date"><svg width="14" height="14" viewBox="0 0 14 14"><rect x="1" y="2" width="12" height="11" fill="none" stroke="#f0861d" stroke-width="1.5"/><path d="M1 5 H13" stroke="#f0861d" stroke-width="1.5"/></svg>01-04-2022</div>
    <div class="card-title">Nemo enim ipsam voluptatem quia</div>
    <div class="card-text">Nemo enim ipsam voluptatem quia voluptas sit aspe rnatur aut odit aut fugit, sed quia consequlupta untr magni dolores oluptatem se.</div>
    <div class="card-more">READ MORE</div>
  </div>
</div>
<div class="card" style="left:626px">
  <div class="card-photo" style="background:linear-gradient(135deg,#b9bcbb,#7d8788 55%,#4d5557)" role="img" aria-label="Photograph of a speaker presenting to a seated audience"></div>
  <div class="card-body">
    <div class="card-date"><svg width="14" height="14" viewBox="0 0 14 14"><rect x="1" y="2" width="12" height="11" fill="none" stroke="#f0861d" stroke-width="1.5"/><path d="M1 5 H13" stroke="#f0861d" stroke-width="1.5"/></svg>01-04-2022</div>
    <div class="card-title">Nemo enim ipsam voluptatem quia</div>
    <div class="card-text">Nemo enim ipsam voluptatem quia voluptas sit aspe rnatur aut odit aut fugit, sed quia consequlupta untr magni dolores oluptatem se.</div>
    <div class="card-more">READ MORE</div>
  </div>
</div>
<div class="btn" style="left:525px;top:3994px;width:150px;height:54px">View more</div>

<!-- partners -->
<div class="abs heading center" style="top:4198px"><strong>Our</strong> partners</div>
<svg class="abs" style="left:56px;top:4325px" width="16" height="26" viewBox="0 0 16 26"><path d="M13 2 L3 13 L13 24" stroke="#555" stroke-width="2.5" fill="none"/></svg>
<svg class="abs" style="left:1128px;top:4325px" width="16" height="26" viewBox="0 0 16 26"><path d="M3 2 L13 13 L3 24" stroke="#555" stroke-width="2.5" fill="none"/></svg>
<div class="partner" style="left:112px"><div class="partner-shape" style="width:120px;height:36px;border-radius:18px"></div></div>
<div class="partner" style="left:310px"><div class="partner-shape" style="width:130px;height:24px"></div></div>
<div class="partner active" style="left:507px"><div class="partner-shape" style="width:136px;height:40px;background:none;border:3px solid #c9c9c9"></div></div>
<div class="partner" style="left:704px"><div class="partner-shape" style="width:60px;height:60px;border-radius:50%"></div></div>
<div class="partner" style="left:902px"><div class="partner-shape" style="width:110px;height:30px"></div></div>

<!-- footer -->
<svg class="abs" style="left:0;top:4400px" width="1200" height="60" viewBox="0 0 1200 60" aria-hidden="true"><path d="M0 52 Q600 -10 1200 52 L1200 60 L0 60 Z" fill="#222222"/></svg>
<div class="abs footer"></div>
<div class="abs" style="left:96px;top:4578px;width:300px;text-align:center">
  <div style="width:64px;height:64px;border-radius:50%;background:var(--orange);margin:0 auto 18px"></div>
  <div style="font-family:'Roboto',sans-serif;font-size:40px;letter-spacing:3px;color:#fff;white-space:nowrap">STAFF FALCONS</div>
</div>
<div class="abs foot-text" style="left:112px;top:4770px;display:flex;gap:8px">
  <svg width="12" height="16" viewBox="0 0 12 16" style="margin-top:2px"><path d="M6 0 C2.7 0 0 2.6 0 5.8 C0 10 6 16 6 16 C6 16 12 10 12 5.8 C12 2.6 9.3 0 6 0 Z" fill="#f0861d"/><circle cx="6" cy="6" r="2.2" fill="#222"/></svg>
  <span>14 - 16 Larkspur Lane<br>London E2 4QX</span>
</div>
<div class="abs foot-text" style="left:112px;top:4832px;display:flex;gap:10px;align-items:center">
  <svg width="18" height="13" viewBox="0 0 18 13"><rect width="18" height="13" rx="1" fill="#f0861d"/><path d="M0 1 L9 7 L18 1" stroke="#222" stroke-width="1.5" fill="none"/></svg>hq@thestafffalcons.co.uk
</div>

<div class="abs foot-title" style="left:491px;top:4566px">Quick Links</div>
<ul class="abs foot-links" style="left:491px;top:4614px"><li>Home</li><li>Our Story</li><li>Newsletter</li><li>Events</li><li>Partners</li><li>Contact</li></ul>

<div class="abs foot-title" style="left:668px;top:4566px;width:420px">Sign up to receive our bi-weekly newsletter direct to your inbox</div>
<div class="field" style="left:670px;top:4647px">Name</div>
<div class="field" style="left:887px;top:4647px">Email</div>
<div class="field" style="left:670px;top:4705px">Job Title</div>
<div class="field" style="left:887px;top:4705px">Company</div>
<div class="btn" style="left:668px;top:4767px;width:115px;height:44px;font-size:15px">Submit</div>

<div class="abs" style="left:112px;top:4888px;width:978px;height:1px;background:#4a4a4a"></div>
<div class="abs foot-text" style="left:112px;top:4921px;font-size:14px">©2022, Staff Falcons. All rights reserved.</div>
<div class="social" style="left:1006px;top:4914px" aria-label="Circlebook"></div>
<div class="social" style="left:1050px;top:4914px" aria-label="ProLink"></div>

</body>
</html>
```